Birchford Realty Business Card

Business Card:

Somewhere on front of card, please include Broker License Number: 5839162

Website is BirchfordRealty.example

Address is:
7218 Crestover Ave E
Saginaw, MI 48271

I'll let you use creative freedom on the rest; we obviously need Name, Title, Email (@BirchfordRealty.example), Office Phone, Cell Phone.

Don't want any special die-cutting, just a standard size business card.

On the back, include a place for the date and time of an appointment to be written in pen.

Requirements
Must have
• Our logo, attached to email.

```html
<!DOCTYPE html>
<html lang="en">
<head>
<meta charset="utf-8">
<title>Birchford Realty Business Card</title>
<link rel="stylesheet" href="https://fonts.googleapis.com/css2?family=Open+Sans:wght@400;600;700&display=swap">
<style>
  :root {
    --navy: #24237a;
    --navy-light: #3d3c9c;
    --ink-grey: #b9b9bd;
    --text-grey: #55555c;
    --paper: #ffffff;
    --backdrop: #e9e9ec;
    --line: rgba(255,255,255,0.75);
  }
  * { box-sizing: border-box; margin: 0; padding: 0; }
  html, body { width: 1200px; height: 900px; overflow: hidden; }
  body {
    background: var(--backdrop);
    font-family: "Open Sans", Arial, sans-serif;
    position: relative;
  }
  .card {
    position: absolute;
    width: 560px;
    height: 320px;
    left: 320px;
    border-radius: 3px;
    overflow: hidden;
    box-shadow: 0 6px 18px rgba(0,0,0,0.18);
  }
  /* Back side */
  .card-back {
    top: 90px;
    background: linear-gradient(100deg, var(--navy) 0%, var(--navy-light) 100%);
    color: #fff;
  }
  .back-brand {
    position: absolute;
    right: 28px;
    top: 22px;
    font-weight: 700;
    font-size: 20px;
    color: rgba(255,255,255,0.85);
    padding-bottom: 6px;
    border-bottom: 1px solid rgba(255,255,255,0.45);
  }
  .appointment {
    position: absolute;
    left: 30px;
    top: 78px;
    width: 250px;
  }
  .appointment-title {
    font-weight: 700;
    font-size: 12px;
    letter-spacing: 1.5px;
    padding-bottom: 3px;
    border-bottom: 1px solid var(--line);
    display: inline-block;
    margin-bottom: 8px;
  }
  .date-column {
    position: absolute;
    left: 300px;
    top: 68px;
    width: 232px;
  }
  .write-line {
    display: flex;
    align-items: flex-end;
    height: 30px;
    font-size: 12px;
    letter-spacing: 0.5px;
  }
  .write-line .label { width: 42px; flex: none; }
  .write-line .rule { flex: 1; border-bottom: 1px solid var(--line); margin-bottom: 4px; }
  /* Front side */
  .card-front {
    top: 450px;
    background: var(--paper);
  }
  .front-wave { position: absolute; inset: 0; }
  .front-brand {
    position: absolute;
    left: 36px;
    top: 112px;
    font-weight: 700;
    font-size: 30px;
    line-height: 1.2;
    color: var(--navy);
    letter-spacing: -0.5px;
    padding-bottom: 4px;
    border-bottom: 2px solid var(--ink-grey);
  }
  .office-details {
    position: absolute;
    left: 36px;
    top: 170px;
    font-size: 10.5px;
    line-height: 15px;
    color: var(--text-grey);
  }
  .person {
    position: absolute;
    left: 340px;
    top: 30px;
  }
  .person-name { font-weight: 700; font-size: 19px; color: var(--navy); }
  .person-title { font-size: 14px; color: #333; }
  .contacts {
    position: absolute;
    left: 322px;
    top: 186px;
    list-style: none;
    color: #fff;
    font-size: 12.5px;
    white-space: nowrap;
  }
  .contacts li { display: flex; align-items: center; height: 24px; }
  .contacts svg { width: 13px; height: 13px; margin-right: 10px; flex: none; }
</style>
</head>
<body>

<section class="card card-back" aria-label="Card back: appointment card">
  <div class="back-brand">Birchford Realty</div>
  <div class="appointment">
    <div class="appointment-title">APPOINTMENT</div>
    <div class="write-line"><span class="label">MON</span><span class="rule"></span></div>
    <div class="write-line"><span class="label">TUE</span><span class="rule"></span></div>
    <div class="write-line"><span class="label">WED</span><span class="rule"></span></div>
    <div class="write-line"><span class="label">THU</span><span class="rule"></span></div>
    <div class="write-line"><span class="label">FRI</span><span class="rule"></span></div>
    <div class="write-line"><span class="label">SAT</span><span class="rule"></span></div>
  </div>
  <div class="date-column">
    <div class="write-line"><span class="label">DATE</span><span class="rule"></span></div>
    <div class="write-line"><span class="label">DATE</span><span class="rule"></span></div>
    <div class="write-line"><span class="label">DATE</span><span class="rule"></span></div>
    <div class="write-line"><span class="label">DATE</span><span class="rule"></span></div>
    <div class="write-line"><span class="label">DATE</span><span class="rule"></span></div>
    <div class="write-line"><span class="label">DATE</span><span class="rule"></span></div>
  </div>
</section>

<section class="card card-front" aria-label="Card front">
  <svg class="front-wave" viewBox="0 0 560 320" width="560" height="320" aria-hidden="true">
    <defs>
      <linearGradient id="waveFill" x1="0" y1="0" x2="1" y2="0">
        <stop offset="0" stop-color="#24237a"/>
        <stop offset="1" stop-color="#3d3c9c"/>
      </linearGradient>
    </defs>
    <path d="M330,140 C400,100 470,88 560,80" fill="none" stroke="#c8c8cc" stroke-width="6" stroke-linecap="round"/>
    <path d="M0,292 C160,300 240,275 290,205 C345,135 430,112 560,98 L560,320 L0,320 Z" fill="url(#waveFill)"/>
    <path d="M60,310 C190,312 260,290 300,225 C330,180 360,160 400,145" fill="none" stroke="#ffffff" stroke-width="3"/>
  </svg>

  <div class="front-brand">Birchford Realty</div>

  <div class="office-details">
    <div>7218 Crestover Ave E</div>
    <div>Saginaw, MI 48271</div>
    <div>Broker License No. 5839162</div>
  </div>

  <div class="person">
    <div class="person-name">Dana Whitlock</div>
    <div class="person-title">Manager</div>
  </div>

  <ul class="contacts">
    <li>
      <svg viewBox="0 0 14 14"><rect x="3" y="1" width="8" height="12" rx="1.5" fill="none" stroke="#fff" stroke-width="1.4"/><circle cx="7" cy="10.5" r="0.9" fill="#fff"/></svg>
      1-555-014-2297
    </li>
    <li>
      <svg viewBox="0 0 14 14"><path d="M3,1.5 L5.5,1.5 L6.5,4.5 L5,5.8 C5.8,7.6 6.6,8.4 8.2,9.2 L9.5,7.7 L12.5,8.7 L12.5,11.5 C12.5,12.2 11.8,12.8 11,12.6 C6.5,12 2,7.5 1.5,3 C1.4,2.2 2.1,1.5 3,1.5 Z" fill="#fff"/></svg>
      0400 555 218
    </li>
    <li>
      <svg viewBox="0 0 14 14"><circle cx="7" cy="7" r="5.8" fill="none" stroke="#fff" stroke-width="1.2"/><ellipse cx="7" cy="7" rx="2.6" ry="5.8" fill="none" stroke="#fff" stroke-width="1"/><line x1="1.2" y1="7" x2="12.8" y2="7" stroke="#fff" stroke-width="1"/></svg>
      BirchfordRealty.example
    </li>
    <li>
      <svg viewBox="0 0 14 14"><text x="7" y="11.5" text-anchor="middle" font-size="13" font-weight="700" fill="#fff" font-family="Open Sans, sans-serif">@</text></svg>
      dana@BirchfordRealty.example
    </li>
  </ul>
</section>

</body>
</html>
```